We currently have a good logo and we want business cards that can display our logo but also represent our industry - telecom construction - We are a construction company specializing in telecom construction such as installation of fiber optic cable throughout cities and across the country. Nationwide services
We are large enough to handle most any project yet small enough to be a flexible partner and resource.

Target Market(s)

U.S. based telecom carriers and providers

Industry/Entity Type

Construction

Contact Information for Business Card

Business cards should include our logo, phone number and website address. Also, including some information as to our core services would be good.

Colors

Designer to choose colors to be used in the design.

Requirements
Must have
• Colors based on logo
• Must use our logo
• Logo, name, email, website address, phone number
• Tovasco Conduit
• Brent Halvik
• Director of Business Development
• (555) 271-0386
• www.TVSQ-example.com
Nice to have
• Construction services including:
• Small Cell Construction
• Boring/Drilling
• Plowing / Trenching
• Conduit installation
• Fiber pulling
• splicing
• building entries
• Aerial construction
• Aerial Make Ready
• Make Ready Engineering
Should not have
• We are open to ideas

```html
<!DOCTYPE html>
<html lang="en">
<head>
<meta charset="UTF-8">
<title>Tovasco Conduit – Business Card</title>
<link rel="stylesheet" href="https://fonts.googleapis.com/css2?family=Noto+Serif:wght@700&family=Open+Sans:wght@400;700;800&display=swap">
<style>
  :root {
    --bg: #3a3e45;
    --blue-deep: #0d55a8;
    --blue-mid: #1a7fc9;
    --blue-light: #22aee4;
    --blue-text: #1569b8;
    --ink: #3c3c3c;
    --grey-band: #767676;
    --white: #ffffff;
  }
  * { margin: 0; padding: 0; box-sizing: border-box; }
  html, body { width: 1200px; height: 1000px; overflow: hidden; }
  body {
    background: var(--bg);
    font-family: "Open Sans", Arial, sans-serif;
    position: relative;
  }
  .card {
    position: absolute;
    left: 215px;
    width: 770px;
    height: 440px;
    border-radius: 22px;
    overflow: hidden;
  }
  /* Front */
  .card-front {
    top: 30px;
    background: linear-gradient(100deg, var(--blue-deep) 0%, var(--blue-mid) 30%, var(--blue-light) 55%, var(--blue-mid) 78%, var(--blue-deep) 100%);
    display: flex;
    align-items: center;
    justify-content: center;
  }
  .brand {
    display: flex;
    align-items: center;
    gap: 16px;
  }
  .brand-mark {
    width: 34px; height: 34px;
    border-radius: 50%;
  }
  .brand-name {
    font-family: "Open Sans", Arial, sans-serif;
    font-weight: 800;
    text-transform: uppercase;
    letter-spacing: 1px;
  }
  .card-front .brand-mark { background: var(--white); }
  .card-front .brand-name { color: var(--white); font-size: 50px; }

  /* Back */
  .card-back {
    top: 530px;
    background: var(--white);
  }
  .back-brand {
    position: absolute;
    left: 60px; top: 110px;
    width: 330px;
    justify-content: center;
  }
  .card-back .brand-mark { background: var(--blue-text); width: 26px; height: 26px; }
  .card-back .brand-name { color: var(--blue-text); font-size: 30px; line-height: 1.05; }
  .divider {
    position: absolute;
    left: 420px; top: 60px;
    width: 2px; height: 190px;
    background: var(--blue-text);
  }
  .contact {
    position: absolute;
    left: 450px; top: 62px;
  }
  .person-name {
    font-family: "Noto Serif", Georgia, serif;
    font-weight: 700;
    color: var(--blue-text);
    font-size: 36px;
    line-height: 1.1;
  }
  .person-title {
    color: var(--ink);
    font-size: 17px;
    margin: 4px 0 14px;
  }
  .contact-list { list-style: none; }
  .contact-list li {
    display: flex; align-items: center; gap: 10px;
    color: var(--ink);
    font-size: 21px;
    line-height: 1.45;
  }
  .contact-list svg { width: 16px; height: 16px; flex: none; }
  .services {
    position: absolute;
    left: 42px; top: 290px;
    list-style: none;
    display: flex; flex-wrap: wrap;
    width: 700px;
    row-gap: 6px;
  }
  .services li {
    color: var(--ink);
    font-size: 18.5px;
    margin-right: 14px;
    white-space: nowrap;
  }
  .services li::before {
    content: "•";
    color: var(--blue-text);
    margin-right: 7px;
  }
  .band {
    position: absolute;
    bottom: 0; left: 0; right: 0;
    height: 16px;
    background: linear-gradient(105deg, var(--blue-text) 0 48%, var(--white) 48% 49.2%, var(--grey-band) 49.2% 100%);
  }
</style>
</head>
<body>
  <section class="card card-front" aria-label="Card front">
    <div class="brand">
      <span class="brand-mark"></span>
      <span class="brand-name">Tovasco Conduit</span>
    </div>
  </section>

  <section class="card card-back" aria-label="Card back">
    <div class="brand back-brand">
      <span class="brand-mark"></span>
      <span class="brand-name">Tovasco<br>Conduit</span>
    </div>

    <div class="divider"></div>

    <div class="contact">
      <h1 class="person-name">Brent Halvik</h1>
      <p class="person-title">Director of Business Development</p>
      <ul class="contact-list">
        <li>
          <svg viewBox="0 0 16 16" fill="none" stroke="#1569b8" stroke-width="1.6"><rect x="4" y="1" width="8" height="14" rx="1.5"/><line x1="7" y1="12.5" x2="9" y2="12.5"/></svg>
          (555) 271-0386
        </li>
        <li>
          <svg viewBox="0 0 16 16" fill="none" stroke="#1569b8" stroke-width="1.6"><rect x="1" y="3" width="14" height="10" rx="1"/><polyline points="1,3 8,9 15,3"/></svg>
          contact@TVSQ-example.com
        </li>
        <li>
          <svg viewBox="0 0 16 16" fill="none" stroke="#1569b8" stroke-width="1.4"><circle cx="8" cy="8" r="6.5"/><ellipse cx="8" cy="8" rx="3" ry="6.5"/><line x1="1.5" y1="8" x2="14.5" y2="8"/></svg>
          www.TVSQ-example.com
        </li>
      </ul>
    </div>

    <ul class="services">
      <li>Small Cell Construction</li>
      <li>Boring/Drilling</li>
      <li>Plowing / Trenching</li>
      <li>Conduit installation</li>
      <li>Fiber pulling</li>
      <li>Splicing</li>
      <li>Building entries</li>
      <li>Aerial construction</li>
      <li>Aerial Make Ready</li>
    </ul>

    <div class="band"></div>
  </section>
</body>
</html>
```